Kip's Pharmacy Business Card Design Project

I need a business card designed for my pharmacy Kip's Pharmacy. I would like just the logo on one side, maybe with black background and white lettering. The other side I would also like to include my logo which is attached. Also, please include my name and the following information:
Rolf Mayhew Owner/Pharm D.
Business address is 7314 N Birchwood Rd Harlow Bend, MN 57193.
Phone number is 218-318-2067 and fax # is 218-318-2063.
my email address is kip@kipsrxhall.com.
My website is www.kipsrxhall.com.
Our store hours run Monday-Friday 9am-6 pm. Saturday 9am-1 pm. Sunday Closed.
I would like the design to include my logo colors, black, white, and neon green. Silver may be added as a highlight. Thanks.
Industry/Entity Type
Pharmacy
Contact Information for Business Card
See above in product description
Look and feel

```html
<!DOCTYPE html>
<html lang="en">
<head>
<meta charset="utf-8">
<title>Kip's Pharmacy – Business Card</title>
<link rel="stylesheet" href="https://fonts.googleapis.com/css2?family=Open+Sans:wght@400;600&display=swap">
<style>
  :root {
    --backdrop: #e9e7e2;
    --card-black: #0b0b0b;
    --card-black-hi: #2a2a2a;
    --card-white: #ffffff;
    --card-white-shade: #e6e6e6;
    --neon-green: #1f9a4d;
    --lime: #8cc63f;
    --ink: #1a1a1a;
    --silver: #c9c9c9;
    --title-gold: #e0a21b;
  }
  * { box-sizing: border-box; margin: 0; padding: 0; }
  html, body { width: 1200px; height: 900px; overflow: hidden; }
  body {
    background: var(--backdrop);
    font-family: "Open Sans", Arial, sans-serif;
    position: relative;
  }
  .card {
    position: absolute;
    width: 580px;
    height: 332px;
    border-radius: 2px;
    box-shadow: 0 10px 28px rgba(0,0,0,.22);
    overflow: hidden;
  }

  /* ---------- Contact side ---------- */
  .card--contact {
    left: 70px; top: 90px;
    background: linear-gradient(155deg, var(--card-black-hi) 0%, var(--card-black) 45%, #000 100%);
    color: #fff;
  }
  .brand {
    position: absolute;
    display: flex;
    align-items: center;
  }
  .brand__dot {
    width: 30px; height: 30px;
    border-radius: 50%;
    background: var(--lime);
    flex: none;
  }
  .brand__rule {
    width: 1px; height: 46px;
    margin: 0 16px;
  }
  .brand__name {
    font-weight: 600;
    letter-spacing: -0.5px;
    white-space: nowrap;
  }
  .card--contact .brand { left: 250px; top: 40px; }
  .card--contact .brand__rule { background: var(--silver); }
  .card--contact .brand__name { font-size: 30px; color: #fff; }

  .owner {
    position: absolute;
    left: 34px; top: 190px;
  }
  .owner__name {
    font-size: 17px;
    font-weight: 600;
    letter-spacing: .5px;
    color: var(--silver);
  }
  .owner__title {
    font-size: 14px;
    color: var(--title-gold);
    margin-top: 2px;
  }

  .contact-list {
    position: absolute;
    left: 250px; top: 128px;
    list-style: none;
  }
  .contact-list li {
    display: flex;
    align-items: center;
    font-size: 14px;
    line-height: 25px;
    color: #f2f2f2;
    white-space: nowrap;
  }
  .contact-list svg {
    width: 13px; height: 13px;
    margin-right: 9px;
    fill: #f2f2f2;
    flex: none;
  }

  .hours-band {
    position: absolute;
    left: 0; right: 0; bottom: 0;
    height: 36px;
    background: var(--neon-green);
    border-top: 2px solid #2fb864;
    color: #fff;
    font-size: 12.5px;
    display: flex;
    align-items: center;
    padding-left: 34px;
    white-space: nowrap;
  }

  /* ---------- Logo side ---------- */
  .card--logo {
    left: 550px; top: 478px;
    background: radial-gradient(circle at 35% 40%, var(--card-white) 0%, var(--card-white) 45%, var(--card-white-shade) 100%);
    color: var(--ink);
  }
  .card--logo .brand { left: 70px; top: 118px; }
  .card--logo .brand__rule { background: #555; height: 60px; }
  .card--logo .brand__name { font-size: 38px; color: var(--ink); }
  .web-line {
    position: absolute;
    left: 70px; bottom: 34px;
    font-size: 13px;
    color: var(--ink);
  }
</style>
</head>
<body>

  <section class="card card--contact" aria-label="Contact side of business card">
    <div class="brand">
      <span class="brand__dot"></span>
      <span class="brand__rule"></span>
      <span class="brand__name">Kip's Pharmacy</span>
    </div>

    <div class="owner">
      <p class="owner__name">ROLF MAYHEW</p>
      <p class="owner__title">Owner/Pharm D</p>
    </div>

    <ul class="contact-list">
      <li>
        <svg viewBox="0 0 16 16" aria-hidden="true"><path d="M8 1 1 7.5h2V15h4v-4h2v4h4V7.5h2z"/></svg>
        7314 N Birchwood Rd Harlow Bend, MN 57193.
      </li>
      <li>
        <svg viewBox="0 0 16 16" aria-hidden="true"><path d="M4 1 6.5 4 5 6c1 2 3 4 5 5l2-1.5 3 2.5-1.5 2.5C8 14.5 1.5 8 2 2.5z"/></svg>
        218-318-2067
      </li>
      <li>
        <svg viewBox="0 0 16 16" aria-hidden="true"><path d="M4 1h7v4H4zM1 6h14v7h-3v2H4v-2H1zm4 5v3h6v-3z"/></svg>
        218-318-2063.
      </li>
      <li>
        <svg viewBox="0 0 16 16" aria-hidden="true"><path d="M1 3h14v10H1zm1.5 1.5v.3L8 9l5.5-4.2v-.3zm0 2.2v4.8h11V6.7L8 11z"/></svg>
        kip@kipsrxhall.com.
      </li>
      <li>
        <svg viewBox="0 0 16 16" aria-hidden="true"><path d="M8 1a7 7 0 1 0 0 14A7 7 0 0 0 8 1zm0 1.5c.8 0 1.8 1.6 2.1 4.5H5.9C6.2 4.1 7.2 2.5 8 2.5zM2.6 7h1.9c0-1.5.3-2.9.8-3.9A5.5 5.5 0 0 0 2.6 7zm8.9 0h1.9a5.5 5.5 0 0 0-2.7-3.9c.5 1 .8 2.4.8 3.9zM2.6 9a5.5 5.5 0 0 0 2.7 3.9c-.5-1-.8-2.4-.8-3.9zm3.3 0c.3 2.9 1.3 4.5 2.1 4.5s1.8-1.6 2.1-4.5zm5.6 0c0 1.5-.3 2.9-.8 3.9A5.5 5.5 0 0 0 13.4 9z"/></svg>
        www.kipsrxhall.com.
      </li>
    </ul>

    <p class="hours-band">Our store hours run Monday-Friday 9am-6 pm. Saturday 9am-1 pm. Sunday Closed.</p>
  </section>

  <section class="card card--logo" aria-label="Logo side of business card">
    <div class="brand">
      <span class="brand__dot"></span>
      <span class="brand__rule"></span>
      <span class="brand__name">Kip's Pharmacy</span>
    </div>
    <p class="web-line">www.kipsrxhall.com</p>
  </section>

</body>
</html>
```